Brightmoor Snacks needs a label design

I need a design for a label on a snacks company packets/containers.
we manufacture Indian snacks.
The label should be green in color and must have background image of indian snacks on it.
Updates

Project Deadline Extended
Reason: Extension of 5 days due to lack of design submission by Designers

Target Market(s)

Groceries Supermarkets

Industry/Entity Type

Food Store

Font styles to use
Script

Colors
9bcb3c

Requirements
Must have
• Similar setup as Tavlor Snacks see attachment below of Tavlors Packet
Nice to have
• Indian snacks in background in dull colors but visible image as I would print ingredients list and other information such as nutritional info
Should not have

```html
<!DOCTYPE html>
<html lang="en">
<head>
<meta charset="utf-8">
<title>Brightmoor Snacks – Hot Mix Bhuja Label</title>
<link href="https://fonts.googleapis.com/css2?family=Open+Sans:wght@400;600;700&family=Roboto+Condensed:wght@400;700&display=swap" rel="stylesheet">
<style>
  :root {
    --backdrop: #6b7a2e;
    --label-green: #3c9a4d;
    --deep-green: #1d6a36;
    --weight-green: #2f9447;
    --snack-cream-1: #efe9d6;
    --snack-cream-2: #f6f2e6;
    --snack-green-1: #2e8f45;
    --snack-green-2: #4ba85a;
    --white: #ffffff;
    --ink: #111111;
  }
  * { box-sizing: border-box; margin: 0; padding: 0; }
  html, body { width: 1200px; height: 1200px; overflow: hidden; }
  body {
    background: var(--backdrop);
    font-family: "Open Sans", Arial, sans-serif;
    position: relative;
  }
  .label {
    position: absolute;
    left: 75px; top: 366px;
    width: 1050px; height: 468px;
    background: var(--label-green);
    border-radius: 30px;
    overflow: hidden;
  }
  .snack-photo-top {
    position: absolute;
    left: 14px; top: 14px;
    width: 1022px; height: 234px;
    border-radius: 16px 16px 0 0;
    background: linear-gradient(120deg, var(--snack-cream-1), var(--snack-cream-2) 45%, #e6dfc6 80%, var(--snack-cream-2));
  }
  .snack-photo-bottom {
    position: absolute;
    left: 14px; top: 248px;
    width: 1022px; height: 206px;
    border-radius: 0 0 16px 16px;
    background: linear-gradient(110deg, var(--snack-green-1), var(--snack-green-2) 50%, var(--snack-green-1));
  }
  .brand-name {
    position: absolute;
    left: 0; right: 0; top: 40px;
    text-align: center;
    font-weight: 700;
    font-size: 76px;
    line-height: 1;
    color: var(--deep-green);
  }
  .net-weight {
    position: absolute;
    right: 28px; top: 30px;
    font-weight: 600;
    font-size: 27px;
    color: var(--weight-green);
  }
  .product-name {
    position: absolute;
    left: 0; right: 0; top: 188px;
    text-align: center;
    font-weight: 700;
    font-size: 52px;
    line-height: 1;
    color: var(--deep-green);
  }
  .ingredients {
    position: absolute;
    left: 14px; top: 264px;
    font-weight: 600;
    font-size: 33px;
    color: var(--white);
  }
  .company {
    position: absolute;
    left: 28px; top: 383px;
    font-weight: 600;
    font-size: 26px;
    color: var(--white);
  }
  .company-note {
    position: absolute;
    left: 34px; top: 420px;
    font-size: 22px;
    color: var(--white);
  }
  .nutrition {
    position: absolute;
    left: 761px; top: 270px;
    width: 263px; height: 186px;
    background: var(--white);
    padding: 4px 10px;
    font-family: "Roboto Condensed", Arial, sans-serif;
    color: var(--ink);
    font-size: 11.5px;
    line-height: 1.25;
  }
  .nutrition-title {
    font-weight: 700;
    font-size: 31px;
    line-height: 1.05;
    border-bottom: 2px solid var(--ink);
    padding-left: 6px;
  }
  .nutrition-row { display: flex; justify-content: space-between; padding: 0 4px; }
  .nutrition-row.indent { padding-left: 16px; }
  .rule-thick { border-bottom: 3px solid var(--ink); margin: 2px 4px; }
  .rule-thin { border-bottom: 1px solid var(--ink); margin: 1px 4px; }
  .right { justify-content: flex-end; }
</style>
</head>
<body>
  <section class="label">
    <div class="snack-photo-top" role="img" aria-label="Faded photograph of cream-coloured bhuja sev and mixed Indian snacks"></div>
    <div class="snack-photo-bottom" role="img" aria-label="Green-tinted photograph of bhuja sev and mixed Indian snacks"></div>

    <div class="brand-name">Brightmoor</div>
    <div class="net-weight">350 Grams</div>
    <h1 class="product-name">HOT MIX BHUJA</h1>

    <p class="ingredients">Ingredients : Nuts, Peas, Corn, Snack. etc.</p>
    <p class="company">BRIGHTMOOR FOODS PTY. LTD.</p>
    <p class="company-note">Lorem ipsum dolor sit amet, sea errem vocibus</p>

    <div class="nutrition">
      <div class="nutrition-title">Nutrition Facts</div>
      <div class="nutrition-row">Amount Per Serving</div>
      <div class="rule-thick"></div>
      <div class="nutrition-row"><span>Calories 45</span><span>Calories from Fat 27g</span></div>
      <div class="rule-thin"></div>
      <div class="nutrition-row right"><span>% Daily Value*</span></div>
      <div class="rule-thin"></div>
      <div class="nutrition-row"><span>Total Fat 301g</span><span>5%</span></div>
      <div class="nutrition-row indent"><span>Saturated Fat 0.44g</span><span>2%</span></div>
      <div class="nutrition-row indent"><span>Trans Fat 0g</span><span></span></div>
      <div class="rule-thin"></div>
      <div class="nutrition-row"><span>Cholesterol &nbsp;0mg</span><span>0%</span></div>
      <div class="nutrition-row"><span>Sodium 17mg</span><span>1%</span></div>
    </div>
  </section>
</body>
</html>
```